Nutrition Company Needs Labels That Define Brand

Natural health supplement company looking for label designs that can define brand. Bold, Clean, Crisp. Product is Apple Cider Vinegar Gummies. Bottle will be clear, colors suggested are white, red, black, green, gold. All colors don't need to used, just suggestions. Apple images, icons welcomed. Will send examples of working design as requested. In progress design below

Target Market(s)

25-65+ Health Conscious, Energetic and Active lifestyle.

Font styles to use
Sans Serif

Colors
ec1f27
f04a50
f59296
87d0c7
17b099
86cfc6
ffffff
ffc214
ffcf3e

Requirements
Must have
• ⚠ IMPORTANT ⚠
Design in a CMYK format (not RGB).
Upload the label without the “Information” layer (DELETE this layer, including the Bleed & Safe outlines).
All vector text and pathways should be converted to outlines.
Save the file as a PDF
Ensure all product claims have this symbol † after them
DO NOT MODIFY FORMATTING OR FONT SIZES ON THE FACTS PANEL.
SAFE ZONE:
All critical elements (text, images, graphic elements, logos, etc.) must be kept inside the red line. Anything left outside of the red area may be cut off during printing.

BLEED ZONE:
Make sure to extend the background artwork, images or colors to the edge of the blue outline.

SKU / BARCODE:
A unique barcode will be applied to your label in the area marked. Do not apply any color, images or graphics in this area as they will be overwritten. Remove the text "Bar-Code Zone" and leave this area white and clear of any artwork.

QHR PRODUCT CLAIMS:
All product claims (for example, "Lose Weight...") need to have this symbol † after them which references the "These statements have not been evaluated by the QHR..." disclaimer. This is a requirement by the QHR.

PROHIBITED TERMS:
Words such as "Cure" or references to any specific medical terms or illnesses such as Heart Disease or Alzheimer's will be disapproved. Instead use more general terms such as "Supports Your Cardiovascular Health" or "Can Improve Memory Loss".

Products can not be labelled Organic, but they can be called "Natural".

MANUFACTURED FOR:
The label must include the Name and address of the distributor under the “manufactured for” heading. It must also include the Street address if the firm name and address are not listed in a current city directory or telephone book, as well as the City or Town, State, and ZIP code.
Nice to have
• Colors are suggested but not set in stone.
Should not have
• Gimmicky designs, logos etc.

```html
<!DOCTYPE html>
<html lang="en">
<head>
<meta charset="utf-8">
<title>Solvara Nutrition – Apple Cider Vinegar Gummies Labels</title>
<link href="https://fonts.googleapis.com/css2?family=Montserrat:wght@400;700&family=Saira+Semi+Condensed:wght@400;500&family=Roboto+Condensed:wght@400;700&family=Kaushan+Script&display=swap" rel="stylesheet">
<style>
  :root {
    --bg: #ececec;
    --white: #ffffff;
    --ink: #1a1a1a;
    --cyan: #17c4f2;
    --cyan-light: #4ee6ff;
    --lime: #8cc63f;
    --lime-light: #d8f0a8;
    --leaf: #3aa63a;
    --red: #ec1f27;
    --red-mid: #f04a50;
    --pink: #f59296;
    --black: #111111;
  }
  * { box-sizing: border-box; margin: 0; padding: 0; }
  html, body { width: 1200px; height: 942px; overflow: hidden; background: var(--bg); }
  .canvas {
    position: relative; width: 1200px; height: 942px;
    display: flex; justify-content: center; align-items: center; gap: 60px;
  }
  .label {
    position: relative; width: 500px; height: 560px; overflow: hidden;
    background: var(--white); box-shadow: 0 6px 24px rgba(0,0,0,.12);
  }
  .label svg.art { position: absolute; inset: 0; }
  .brand {
    position: absolute; left: 135px; top: 62px; white-space: nowrap;
    font-family: "Montserrat", sans-serif; font-weight: 700; font-size: 26px;
    color: var(--ink); display: flex; align-items: center; gap: 10px;
  }
  .brand .dot { width: 20px; height: 20px; border-radius: 50%; background: var(--leaf); }
  .label--red .brand .dot { background: var(--red); }
  .title {
    position: absolute; right: 55px; top: 212px; text-align: right; white-space: nowrap;
    font-family: "Saira Semi Condensed", sans-serif; font-weight: 500; line-height: 1;
  }
  .title .line1 { font-size: 46px; color: var(--leaf); }
  .title .line2 { font-size: 46px; color: var(--ink); margin-right: 36px; margin-top: 6px; }
  .label--red .title .line1 { color: var(--red); }
  .script {
    position: absolute; left: 75px; top: 312px; white-space: nowrap;
    font-family: "Kaushan Script", cursive; font-size: 98px; line-height: 1;
    color: var(--black); text-shadow: 2px 2px 0 var(--white), -1px -1px 0 var(--white);
  }
  .count {
    position: absolute; left: 8px; top: 380px; text-align: center;
    font-family: "Roboto Condensed", sans-serif; color: var(--cyan); line-height: .95;
  }
  .count .num { font-size: 40px; font-weight: 700; display: block; }
  .count .unit { font-size: 13px; color: var(--ink); }
  .label--red .count .num, .label--red .count .unit { color: var(--white); }
  .tagline {
    position: absolute; left: 150px; top: 420px; white-space: nowrap;
    font-family: "Saira Semi Condensed", sans-serif; font-size: 24px; line-height: 1; color: var(--ink);
  }
  .label--red .tagline { color: var(--white); }
  .supplement {
    position: absolute; left: 12px; top: 482px; white-space: nowrap;
    font-family: "Roboto Condensed", sans-serif; font-weight: 700; font-size: 28px;
    color: var(--white); transform: rotate(2deg);
  }
  .badge {
    position: absolute; left: 416px; top: 420px; width: 62px; height: 62px;
    border-radius: 50%; border: 3px solid var(--white);
  }
</style>
</head>
<body>
<main class="canvas">

  <section class="label label--blue">
    <svg class="art" width="500" height="560" viewBox="0 0 500 560">
      <defs>
        <linearGradient id="fadeBlue" x1="0" y1="0" x2="0" y2="1">
          <stop offset="0.3" stop-color="#ffffff"/>
          <stop offset="1" stop-color="#d8f0a8"/>
        </linearGradient>
        <linearGradient id="swoopBlue" x1="0" y1="0" x2="1" y2="1">
          <stop offset="0" stop-color="#17c4f2"/>
          <stop offset="1" stop-color="#4ee6ff"/>
        </linearGradient>
      </defs>
      <rect width="500" height="560" fill="url(#fadeBlue)"/>
      <path d="M500 0 L500 560 L430 560 C500 420 500 200 420 120 C380 160 350 200 330 200 C380 140 430 60 500 0 Z" fill="url(#swoopBlue)"/>
      <g role="img" aria-label="Stylised apple illustration in cyan">
        <path d="M0 80 C55 70 110 110 118 180 C124 260 80 330 25 350 C12 354 4 350 0 345 Z" fill="#17c4f2"/>
      </g>
      <path d="M0 470 C150 450 300 462 500 455 L500 560 L0 560 Z" fill="#8cc63f"/>
      <path d="M220 560 C320 500 420 475 500 440 L500 560 Z" fill="#17c4f2"/>
    </svg>
    <div class="brand"><span class="dot"></span>Solvara Nutrition</div>
    <div class="title"><div class="line1">APPLE CIDER</div><div class="line2">VINEGAR</div></div>
    <div class="script">Gummies</div>
    <div class="count"><span class="num">60</span><span class="unit">GUMMIES</span></div>
    <div class="tagline">RAW &amp; UNFILTERED</div>
    <div class="supplement">Dietary Supplement</div>
    <div class="badge"></div>
  </section>

  <section class="label label--red">
    <svg class="art" width="500" height="560" viewBox="0 0 500 560">
      <defs>
        <linearGradient id="fadeRed" x1="0" y1="0" x2="0" y2="1">
          <stop offset="0.3" stop-color="#ffffff"/>
          <stop offset="1" stop-color="#f04a50"/>
        </linearGradient>
        <linearGradient id="swoopRed" x1="0" y1="0" x2="1" y2="1">
          <stop offset="0" stop-color="#ec1f27"/>
          <stop offset="1" stop-color="#f04a50"/>
        </linearGradient>
      </defs>
      <rect width="500" height="560" fill="url(#fadeRed)"/>
      <path d="M500 0 L500 560 L430 560 C500 420 500 200 420 120 C380 160 350 200 330 200 C380 140 430 60 500 0 Z" fill="url(#swoopRed)"/>
      <g role="img" aria-label="Stylised apple illustration in red">
        <path d="M0 80 C55 70 110 110 118 180 C124 260 80 330 25 350 C12 354 4 350 0 345 Z" fill="#ec1f27"/>
      </g>
      <path d="M0 470 C150 450 300 462 500 455 L500 560 L0 560 Z" fill="#111111"/>
      <path d="M220 560 C320 500 420 475 500 440 L500 560 Z" fill="#ec1f27"/>
    </svg>
    <div class="brand"><span class="dot"></span>Solvara Nutrition</div>
    <div class="title"><div class="line1">APPLE CIDER</div><div class="line2">VINEGAR</div></div>
    <div class="script">Gummies</div>
    <div class="count"><span class="num">60</span><span class="unit">GUMMIES</span></div>
    <div class="tagline">RAW &amp; UNFILTERED</div>
    <div class="supplement">Dietary Supplement</div>
    <div class="badge"></div>
  </section>

</main>
</body>
</html>
```